Design an IT/hosting company homepage in Visual Composer (WordPress)

Hi,

we are building our new site. We are looking for a fantastic homepage design.

We don't know what we want exactly on our homepage, so we'll leave it up to your suggestions. What we think that should be there:
- A slider (we want you to create some sample slides as well)
- Our most important services (see below).
- Some images and/or icons
- Some written content
- Call to actions
- ...

The design has to be in line with the branding an other pages we already have in place. It has to be eye catching and contain CTA's.
Our website is created with the Avada theme, and Visual composer is available as well.

Header: [url removed, login to view]
Some example pages:

if you want to see the live website, drop me a message and I'll share the URL.

Following colours are used in our logo:
1: 44A7DE
2: 2194D2
3: 848585
4: 535453

Some info about our company:
• Founded in 2004
• Located in Belgium
• Aiming at private customers & small to mid size companies.
• Pro service at budget price
• Enterprise standards
• On our prio list: 99,9% uptime, fast support, privacy, solid solutions, personal approach
• Fast support via mail, chat & phone, both in Dutch & English
• Team of well-trained engineers
• 1 datacenter in Belgium
• 1 datacenter in Netherlands

Our most important services:

Web hosting starting at €2,5 a month:
• Fast hosting with SSD disks
• Servers in Belgium & Netherlands
• All package include unlimited bandwidth, advanced protection/firewalling, daily backups, and fast support
• Our hosting packages come with a free .be/.nl/.eu/.com domain name, & unlimited email accounts
• When you take a hosting account with us, we provide a free service to move from your old host to us, or we install WordPress, Joomla or Drupal for you

Online Backup
• Backup all your data to the secure cloud
• Recover your data after data loss (crash, theft, fire, …)
• 3 storage options: 5GB, 50GB & unlimited (unlimited is pretty unique)
• Backup of Desk Suite 12 accounts to the secure cloud
• Backups of Norvanta NAS to the secure cloud
• In case of disaster, we can come to your house or office with the backup data
• Starting at 5€ with 5GB storage and €20 with unlimited storage
• No setup costs or fixed contracts. Cancel at any time.
• Free 14 day trial

Virtual Servers start at €10/month:
• Fast SSD VPS servers, based on Quelbix, with premium hardware
• A Virtual Private Server (VPS) is a hosting environment that combines the benefits of shared hosting and dedicated servers.
• Very scalable and flexible. If you need extra resources, these can be added quickly.
• Windows or Linux
• Options available like daily backups (onsite or offsite) or HA setup

Domain names:
• We can register all domain name extensions available
• Realtime registration
• Free 5 GB mailbox and e-mail address
• Free Unlimited number of subdomains
• Free Full control over the DNS settings
• Free Unlimited e-mail aliases for mail forwarding
• Starting at €10/year

Wordpress managed hosting:
• Same as normal hosting, but optimized for Wordpress
• We manage WP for you
• Monthly updates for Wordpress & plugins
• Security hardening

Joomla managed hosting:
• Same as normal hosting, but optimized for Joomla
• We manage Jooma for you
• Monthly updates for Joomla & plugins
• Security hardening

Please submit your mockups & details about your design.
After we choose & award an entry, we'll give you credentials to our website, and you have to create the page as per your entry in WordPress.

Thanks, good luck, and amaze us! :)

```html
<!DOCTYPE html>
<html lang="en">
<head>
<meta charset="utf-8">
<title>Hostvela – Web Hosting</title>
<link href="https://fonts.googleapis.com/css2?family=Roboto:wght@300;400;500;700&display=swap" rel="stylesheet">
<style>
:root{
  --blue:#2194d2;--blue-light:#44a7de;--grey:#848585;--grey-dark:#535453;
  --ink:#333;--muted:#8a8a8a;--dark:#111;--footer:#242424;--footer-bottom:#1a1a1a;
  --panel:#e4e4e4;--white:#fff;
}
*{box-sizing:border-box;margin:0;padding:0}
html,body{width:1200px;height:4045px;overflow:hidden}
body{position:relative;font-family:'Roboto',Arial,sans-serif;color:var(--ink);background:var(--white)}
.abs{position:absolute}
.topbar{left:0;top:0;width:1200px;height:36px;background:#3a3a3a;color:#fff;font-size:11px}
.topbar .social{left:40px;top:11px;display:flex;gap:16px}
.dot{width:12px;height:12px;border-radius:50%;background:#bbb;display:block}
.topbar .contact{left:842px;top:11px;font-weight:500}
.topbar .lang{left:1066px;top:9px;width:94px;height:18px;background:#fff;color:#999;font-size:9px;padding:3px 6px}
.topbar .lang i{position:absolute;right:0;top:0;width:16px;height:18px;background:#555}
.nav{left:0;top:36px;width:1200px;height:61px;background:#fff;border-bottom:4px solid #ddd}
.logo{left:42px;top:14px;font-size:26px;color:var(--blue);font-weight:400}
.menu{right:44px;top:24px;display:flex;gap:24px;font-size:12px;color:#333}
.hero{left:0;top:97px;width:1200px;height:556px;background:radial-gradient(ellipse at 50% 30%,#3b3b3b,#0e0e0e 75%)}
.hero-lead{left:75px;top:240px;font-size:34px;font-weight:300;color:#fff}
.hero-title{left:75px;top:282px;font-size:50px;font-weight:400;color:#fff}
.hero-text{left:76px;top:352px;width:430px;font-size:14px;line-height:30px;color:#fff}
.btn-blue{background:var(--blue);color:#fff;font-size:12px;font-weight:500;text-align:center}
.hero-btn{left:79px;top:445px;width:179px;height:47px;line-height:47px}
.arrow{top:360px;width:20px;height:30px}
.hero-art{left:690px;top:200px;width:490px;height:380px;background:linear-gradient(160deg,#9a9a9a,#3a3a3a);border-radius:6px;opacity:.8}
.price-badge{left:691px;top:322px;width:94px;height:94px;border-radius:50%;background:#fff;text-align:center;font-size:13px;color:#666;padding-top:27px}
.price-badge b{color:var(--blue);font-weight:700}
.panel{background:#fff}
.section-kicker{font-size:25px;font-weight:700;color:var(--blue);text-align:right}
.section-title{font-size:26px;font-weight:500;color:#333;text-align:right}
.vbar{width:4px;background:var(--blue)}
.intro{font-size:13px;line-height:22px;color:#8a8a8a}
.svc{width:345px;height:137px;background:var(--panel)}
.svc.active{background:var(--blue);color:#fff}
.svc .ic{left:20px;top:22px;width:70px;height:70px;border-radius:50%;background:#fff}
.svc h3{left:111px;top:18px;width:210px;font-size:19px;font-weight:400;color:#333;line-height:21px}
.svc p{left:111px;top:70px;width:220px;font-size:13px;color:#8a8a8a;line-height:22px}
.svc.active h3,.svc.active p{color:#fff}
.dark-band{left:0;top:1166px;width:1200px;height:632px;background:radial-gradient(ellipse at 60% 40%,#262626,#050505 70%)}
.tab{top:1261px;height:104px;background:#fff;text-align:center;font-size:13px;font-weight:500;color:#333;border-right:1px solid #ccc;padding-top:70px}
.tab.active{background:var(--blue);color:#fff}
.tab svg{position:absolute;left:50%;top:18px;transform:translateX(-50%)}
.offer-title{left:613px;top:1432px;font-size:33px;color:#fff;font-weight:300}
.offer-title b{color:var(--blue);font-weight:500}
.offer-text{left:613px;top:1490px;width:520px;font-size:13.5px;line-height:24px;color:#fff}
.checks{font-size:11.5px;color:#fff;line-height:27px}
.btn-grey{background:var(--grey);color:#fff;font-size:12px;text-align:center}
.card{background:#fff;box-shadow:0 2px 8px rgba(0,0,0,.18);text-align:center}
.card h4{margin-top:32px;font-size:19px;font-weight:400;color:#555}
.card .band{height:68px;margin-top:22px;background:var(--blue);color:#fff;font-size:38px;font-weight:300;line-height:68px}
.card .band small{font-size:16px}
.card.featured .band{background:var(--grey-dark)}
.card ul{list-style:none;margin-top:14px;font-size:13.5px;color:#888;line-height:35px}
.card .order{display:inline-block;margin-top:16px;width:133px;height:43px;line-height:43px;background:var(--grey-dark);color:#fff;font-size:13px}
.card.featured .order{background:var(--blue)}
.promo-band{left:0;top:2458px;width:1200px;height:542px;background:linear-gradient(120deg,#1c1c1c,#2f2a22 50%,#111)}
.promo{left:42px;top:2534px;width:556px;height:388px;background:var(--blue);border:3px solid var(--blue);outline:2px solid #fff;outline-offset:-8px}
.avail{left:598px;top:2534px;width:560px;height:388px;background:#f1f1f1}
.kick-sm{font-size:12px;font-weight:700;text-align:center}
.big{font-size:27px;font-weight:700;text-align:center}
.feature-list{left:292px;top:120px;font-size:14px;color:#fff;line-height:33.4px}
.feature-list span{display:inline-block;width:12px;height:12px;background:#fff;margin-right:6px;vertical-align:-1px;position:relative}
.feature-list span:after{content:"";position:absolute;left:3px;top:1px;width:4px;height:7px;border:solid var(--blue);border-width:0 2px 2px 0;transform:rotate(45deg)}
.dom{left:44px;width:472px;height:32px;background:var(--grey);color:#fff;font-size:13px;font-weight:700;line-height:32px;padding-left:14px}
.dom b{position:absolute;right:0;top:0;width:104px;height:32px;background:#3d3d3d;padding-left:18px}
.client{font-size:25px;font-weight:300;color:#444;display:flex;align-items:center;gap:6px}
.client i{width:26px;height:26px;background:#444;display:block}
.footer{left:0;top:3463px;width:1200px;height:519px;background:var(--footer);color:#fff}
.fcol{top:100px;width:260px}
.fcol h5{font-size:14px;font-weight:400}
.fcol hr{border:0;width:34px;height:3px;background:var(--blue);margin:8px 0 20px}
.fcol ul{list-style:none;font-size:13.5px;line-height:30px}
.fcol p{font-size:13.5px;line-height:23px}
.store{width:138px;height:46px;border:1px solid #777;border-radius:5px;background:#000}
.email-in{left:597px;top:410px;width:419px;height:47px;background:#fff;color:#aaa;font-size:12px;padding:16px 14px}
.submit{left:1026px;top:410px;width:110px;height:47px;line-height:47px}
.bottom{left:0;top:3982px;width:1200px;height:63px;background:var(--footer-bottom);color:#999;font-size:13px}
.soc{width:32px;height:32px;border-radius:50%;background:#444;top:16px}
</style>
</head>
<body>

<div class="abs topbar">
  <div class="abs social"><i class="dot"></i><i class="dot"></i><i class="dot"></i><i class="dot"></i><i class="dot"></i><i class="dot"></i></div>
  <div class="abs contact">&#9742; +1 (000) 555 0142 &nbsp;|&nbsp; Email Us &nbsp;/</div>
  <div class="abs lang">Belgium<i></i></div>
</div>

<header class="abs nav">
  <div class="abs logo">Hostvela</div>
  <nav class="abs menu"><span>HOME</span><span>HOSTING &amp; DOMAINS</span><span>SERVICES</span><span>ABOUT US</span><span>CONTACT US</span></nav>
</header>

<section class="abs hero" role="img" aria-label="Dark data centre corridor with server racks"></section>
<div class="abs hero-art" role="img" aria-label="Tower server and rack servers"></div>
<div class="abs price-badge">Starts at<br><b>$9.95</b> /mo</div>
<div class="abs hero-lead">We deliver what you need</div>
<h1 class="abs hero-title">SECURE &amp; FAST</h1>
<p class="abs hero-text">Lorem Ipsum is simply dummy text of the printing typesetting industry is proident sunt in culpa officia deserunt mollit.</p>
<div class="abs btn-blue hero-btn">GET STARTED NOW!</div>
<svg class="abs arrow" style="left:30px" viewBox="0 0 20 30"><path d="M15 4 5 15l10 11" stroke="#fff" stroke-width="4" fill="none"/></svg>
<svg class="abs arrow" style="left:1148px" viewBox="0 0 20 30"><path d="M5 4l10 11L5 26" stroke="#fff" stroke-width="4" fill="none"/></svg>

<section class="abs panel" style="left:28px;top:609px;width:1134px;height:557px">
  <div class="abs section-kicker" style="left:0;top:62px;width:384px">WE OFFER</div>
  <div class="abs section-title" style="left:0;top:92px;width:384px">AWESOME SERVICES</div>
  <div class="abs vbar" style="left:410px;top:66px;height:60px"></div>
  <p class="abs intro" style="left:439px;top:63px;width:690px">Lorem ipsum is a dummy text. Lorem ipsum is a dummy text. Lorem ipsum is a dummy text. Lorem ipsum is a dummy text. Lorem ipsum is a dummy text. Lorem ipsum is a dummy text. Lorem ipsum is a dummy text. Lorem ipsum is a dummy text. Lorem ipsum is a dummy text.</p>
</section>

<div class="abs svc" style="left:63px;top:785px">
  <div class="abs ic"><svg width="70" height="70" viewBox="0 0 70 70"><circle cx="35" cy="29" r="7" fill="none" stroke="#999" stroke-width="2"/><path d="M22 47c2-8 24-8 26 0z" fill="none" stroke="#999" stroke-width="2"/></svg></div>
  <h3 class="abs">Team of Well Trained Engineers</h3>
  <p class="abs">Excepteur sit occaecat cupidatan is proident, one sunt in culpa.</p>
</div>
<div class="abs svc" style="left:437px;top:785px">
  <div class="abs ic"><svg width="70" height="70" viewBox="0 0 70 70"><rect x="22" y="25" width="26" height="18" fill="none" stroke="#999" stroke-width="2"/><path d="M19 46h32" stroke="#999" stroke-width="2"/></svg></div>
  <h3 class="abs">Pro Service at Budget Price</h3>
  <p class="abs">Excepteur sit occaecat cupidatan is proident, one sunt in culpa.</p>
</div>
<div class="abs svc active" style="left:63px;top:960px">
  <div class="abs ic"><svg width="70" height="70" viewBox="0 0 70 70"><path d="M26 44l4-10 14-14 6 6-14 14z" fill="none" stroke="#999" stroke-width="2"/></svg></div>
  <h3 class="abs">Full Online Backup Available</h3>
  <p class="abs">Excepteur sit occaecat cupidatan is proident, one sunt in culpa.</p>
</div>
<div class="abs svc" style="left:437px;top:960px">
  <div class="abs ic"><svg width="70" height="70" viewBox="0 0 70 70"><rect x="28" y="22" width="14" height="26" rx="2" fill="none" stroke="#999" stroke-width="2"/></svg></div>
  <h3 class="abs">Fast Support via Mail, Chat &amp; Phone</h3>
  <p class="abs">Excepteur sit occaecat cupidatan is proident, one sunt in culpa.</p>
</div>
<div class="abs" role="img" aria-label="Three server rack cabinets" style="left:815px;top:790px;width:315px;height:305px;background:linear-gradient(180deg,#2a2a2a,#777 80%,#eee)"></div>

<section class="abs dark-band" role="img" aria-label="Dark abstract technology background"></section>
<div class="abs tab active" style="left:143px;width:181px">WEB HOSTING
  <svg width="52" height="44" viewBox="0 0 52 44"><path d="M4 42h44M8 42V26h8v16M22 42V12h8v30M36 42V4h8v38" fill="none" stroke="#fff" stroke-width="2"/></svg></div>
<div class="abs tab" style="left:324px;width:243px">CMS WEBSITE HOSTING
  <svg width="56" height="44" viewBox="0 0 56 44"><rect x="2" y="2" width="52" height="40" fill="none" stroke="#444" stroke-width="2"/><path d="M2 10h52M8 18h16v16H8zM30 18h18M30 24h18M30 30h18" fill="none" stroke="#444" stroke-width="2"/></svg></div>
<div class="abs tab" style="left:567px;width:209px">VIRTUAL SERVERS
  <svg width="48" height="44" viewBox="0 0 48 44"><path d="M24 4 4 14l20 10 20-10zM4 22l20 10 20-10M4 30l20 10 20-10" fill="none" stroke="#444" stroke-width="2"/></svg></div>
<div class="abs tab" style="left:776px;width:198px;border:0">ONLINE BACKUP
  <svg width="56" height="44" viewBox="0 0 56 44"><path d="M2 12V2h10M44 2h10v10M54 32v10H44M12 42H2V32" fill="none" stroke="#444" stroke-width="2"/><rect x="24" y="18" width="8" height="8" fill="none" stroke="#444" stroke-width="2"/></svg></div>
<div class="abs" role="img" aria-label="Row of silver server towers with blue accents" style="left:71px;top:1429px;width:510px;height:236px;background:linear-gradient(180deg,#5a6b85,#c9c9c9 55%,#888);border-radius:4px"></div>
<h2 class="abs offer-title"><b>Web Hosting</b> at € 2,5 / month</h2>
<p class="abs offer-text">Lorem ipsum is a dummy text. Lorem ipsum is a dummy text. Lorem ipsum is a dummy text. Lorem ipsum is a dummy text. Lorem ipsum is a dummy text.</p>
<div class="abs checks" style="left:613px;top:1549px">&#10004; Fast hosting with SSD disks<br>&#10004; Servers in Belgium &amp; Netherlands<br>&#10004; Unlimited email accounts</div>
<div class="abs checks" style="left:873px;top:1549px">&#10004; Free .be/.nl/.eu/.com domain name<br>&#10004; Unlimited bandwidth, Protection/firewalling<br>&#10004; Free service to move from your old host</div>
<div class="abs btn-grey" style="left:613px;top:1654px;width:97px;height:35px;line-height:35px;border-radius:3px">Read More</div>

<section class="abs panel" style="left:31px;top:1798px;width:1131px;height:660px">
  <div class="abs section-kicker" style="left:0;top:54px;width:371px">SELECT YOUR</div>
  <div class="abs section-title" style="left:0;top:84px;width:371px">HOSTING PLATFORMS</div>
  <div class="abs vbar" style="left:401px;top:52px;height:66px"></div>
  <p class="abs intro" style="left:428px;top:51px;width:690px">Lorem ipsum is a dummy text. Lorem ipsum is a dummy text. Lorem ipsum is a dummy text. Lorem ipsum is a dummy text. Lorem ipsum is a dummy text. Lorem ipsum is a dummy text. Lorem ipsum is a dummy text. Lorem ipsum is a dummy text. Lorem ipsum is a dummy text. Lorem ipsum is a dummy text.</p>
</section>

<div class="abs card" style="left:57px;top:1963px;width:249px;height:401px">
  <h4>WEB HOSTING</h4><div class="band">€2,5 <small>/ month</small></div>
  <ul><li>5 GB Storage</li><li>Unlimited projects</li><li>15 Email Accounts</li><li>2 Domain Hosted Support</li><li>24/7 Full Support</li></ul>
  <span class="order">ORDER NOW &#10148;</span></div>
<div class="abs card featured" style="left:322px;top:1944px;width:275px;height:444px;box-shadow:0 6px 18px rgba(0,0,0,.25)">
  <h4>ONLINE BACKUP</h4><div class="band">€5,20 <small>/ month</small></div>
  <ul style="line-height:38px"><li>10 GB Storage</li><li>Unlimited projects</li><li>25 Email Accounts</li><li>2 Domain Hosted Support</li><li>24/7 Full Support</li></ul>
  <span class="order" style="height:48px;line-height:48px">ORDER NOW &#10148;</span></div>
<div class="abs card" style="left:611px;top:1963px;width:250px;height:401px">
  <h4>VIRTUAL SERVERS</h4><div class="band">€10 <small>/ month</small></div>
  <ul><li>30 GB Storage</li><li>Unlimited projects</li><li>35 Email Accounts</li><li>2 Domain Hosted Support</li><li>24/7 Full Support</li></ul>
  <span class="order">ORDER NOW &#10148;</span></div>
<div class="abs card" style="left:887px;top:1963px;width:250px;height:401px">
  <h4>DOMAIN NAMES</h4><div class="band">€10 <small>/ year</small></div>
  <ul><li>Unlimited GB Storage</li><li>Unlimited projects</li><li>Unlimited Email Accounts</li><li>Unlimited Domain Hosted Support</li><li>24/7 Full Support</li></ul>
  <span class="order">ORDER NOW &#10148;</span></div>

<section class="abs promo-band" role="img" aria-label="Dimly lit photo of a person working at a computer"></section>
<div class="abs promo">
  <div class="abs kick-sm" style="left:0;top:56px;width:550px;color:#fff">HOST WITH US</div>
  <div class="abs big" style="left:0;top:76px;width:550px;color:#fff">SPEED UP YOUR SITE</div>
  <div class="abs" role="img" aria-label="Open server rack cabinet" style="left:41px;top:118px;width:197px;height:212px;background:linear-gradient(180deg,#2c2c2c,#666)"></div>
  <div class="abs feature-list"><span></span>Effective Control Panel<br><span></span>Nextgen Hosting<br><span></span>Dedicated Support<br><span></span>Extended Support<br><span></span>Completely Secured<br><span></span>Simple Configuration</div>
</div>
<div class="abs avail">
  <div class="abs kick-sm" style="left:0;top:58px;width:560px;color:#333">NEW DOMAINS</div>
  <div class="abs big" style="left:0;top:78px;width:560px;color:#333">AVAILABLE</div>
  <div class="abs dom" style="top:120px">.com<b>Buy $9.99</b></div>
  <div class="abs dom" style="top:167px">.be<b>Buy $9.99</b></div>
  <div class="abs dom" style="top:214px">.nl<b>Buy $9.99</b></div>
  <div class="abs dom" style="top:262px">.eu<b>Buy $9.99</b></div>
  <div class="abs dom" style="top:309px">.co<b>Buy $9.99</b></div>
</div>

<div class="abs" role="img" aria-label="Laptop showing the homepage" style="left:31px;top:3094px;width:519px;height:299px;background:linear-gradient(180deg,#222,#555 85%,#ccc);border-radius:10px 10px 4px 4px"></div>
<div class="abs" style="left:586px;top:3098px;font-size:12px;font-weight:700;color:#333">FIND OUT OUR</div>
<div class="abs" style="left:586px;top:3114px;font-size:27px;font-weight:700;color:#333">PRECIOUS CLIENTS</div>
<div class="abs client" style="left:586px;top:3170px"><i></i>Brightloom</div>
<div class="abs client" style="left:762px;top:3170px"><i></i>Caldrix</div>
<div class="abs client" style="left:938px;top:3170px"><i></i>Nortessa</div>
<div class="abs client" style="left:586px;top:3240px"><i></i>Pelloran</div>
<div class="abs client" style="left:762px;top:3240px"><i></i>Nortessa</div>
<div class="abs client" style="left:938px;top:3240px"><i></i>Vintaro</div>

<footer class="abs footer">
  <div class="abs fcol" style="left:39px"><h5>ABOUT COMPANY</h5><hr>
    <p>Lorem ipsum is a dummy text. Lorem ipsum is a dummy text. Lorem ipsum is a dummy text. Lorem ipsum is a dummy.</p>
    <p style="margin-top:12px;line-height:36px">&#9679;&nbsp; 48 Harbour Lane, Ostend<br>&#9742;&nbsp; +1 (000) 555 0142<br>&#9993;&nbsp; hello@hostvela.example</p></div>
  <div class="abs fcol" style="left:325px"><h5>SUPPORT</h5><hr>
    <ul><li>› Product Support</li><li>› Report Abuse</li><li>› Knowledgebase</li><li>› Affiliates and Resellers</li><li>› WHOIS Search</li><li>› Scripting &amp; Add-ons</li></ul></div>
  <div class="abs fcol" style="left:611px"><h5>RESOURCES</h5><hr>
    <ul><li>› Email Services</li><li>› WHOIS Search</li><li>› Scripting &amp; Add-ons</li><li>› Marketing Services</li><li>› Affiliates</li><li>› Knowledgebase</li></ul></div>
  <div class="abs fcol" style="left:897px"><h5>ACCOUNT</h5><hr>
    <ul><li>› My Account</li><li>› My Renewals</li><li>› Create Account</li><li>› Knowledgebase</li><li>› Contact Us</li><li>› Affiliates and Resellers</li></ul></div>
  <div class="abs" style="left:39px;top:386px;font-size:12px">Find Us on</div>
  <div class="abs store" style="left:39px;top:410px"></div>
  <div class="abs store" style="left:184px;top:410px"></div>
  <div class="abs" style="left:597px;top:386px;font-size:12px">Sign up for Special Offers!</div>
  <div class="abs email-in">Enter your Email</div>
  <div class="abs btn-blue submit">SUBMIT</div>
</footer>
<div class="abs bottom">
  <div class="abs" style="left:39px;top:24px">Copyright © 2016 hostvela.example. All rights reserved.</div>
  <i class="abs soc" style="left:904px"></i><i class="abs soc" style="left:945px"></i><i class="abs soc" style="left:987px"></i><i class="abs soc" style="left:1028px"></i><i class="abs soc" style="left:1070px"></i><i class="abs soc" style="left:1111px"></i>
</div>
</body>
</html>
```